Marcus Lindqvist Photography needs a business card designs

I am looking for a business card with a logo clean and simple which I can use that logo on my website or on my pictures. It has to be very classy and very professional. Please look at my website at www.marcuslvqphoto.com for my signature. I'm thinking of something like that for my signature/logo. I'm still working on my website but you get an idea. I'm open to any design but not too busy graphics.

I will be printing the business card from qrivel.com.

Surprise me :)

contact me if you have any questions.

-ML

I'm receiving a lot of black background at the moment. I know my website is all black doesn't mean I want my card to be all black. Please send in with some white background as well. Thanks :)

check out some business cards that I found online. I think they are simple and look really awesome. I don't want a card that is too busy.

http://www.marcuslvqphoto.com/p270092084

Reason: Please extend the date for me. I haven't really receive any good design yet.

Printing

• -a logo that related to my first and last initial of my name "ML"
-double sided
• -I don't want my background to be all black.
-no pictures on the card

```html
<!DOCTYPE html>
<html lang="en">
<head>
<meta charset="utf-8">
<title>Marcus Lindqvist Photography — Business Card</title>
<link rel="stylesheet" href="https://fonts.googleapis.com/css2?family=Montserrat:wght@600;800&display=swap">
<style>
  :root {
    --page: #ffffff;
    --card-mid: #464a4d;
    --card-dark: #2b2d2f;
    --card-edge: #1e2021;
    --paper: #ffffff;
    --paper-shade: #dcdedf;
    --strip: #151617;
    --accent: #f0380e;
    --light: #ffffff;
    --ink: #3a3d40;
    --muted: #c9c9c9;
  }
  * { margin: 0; padding: 0; box-sizing: border-box; }
  html, body {
    width: 1200px; height: 370px; overflow: hidden;
    background: var(--page);
    font-family: "Montserrat", "Helvetica Neue", Arial, sans-serif;
  }
  .sheet { position: relative; width: 1200px; height: 370px; }
  .card {
    position: absolute; top: 11px;
    width: 578px; height: 347px; overflow: hidden;
  }
  .card--front {
    left: 11px;
    background:
      radial-gradient(ellipse 60% 22% at 50% 24%, rgba(0,0,0,0.45), rgba(0,0,0,0) 100%),
      radial-gradient(ellipse 55% 14% at 50% 62%, rgba(0,0,0,0.35), rgba(0,0,0,0) 100%),
      radial-gradient(ellipse 75% 70% at 50% 45%, var(--card-mid) 0%, var(--card-dark) 70%, var(--card-edge) 100%);
  }
  .card--back {
    left: 606px;
    background:
      radial-gradient(ellipse 60% 22% at 50% 24%, rgba(0,0,0,0.08), rgba(0,0,0,0) 100%),
      radial-gradient(ellipse 75% 70% at 50% 45%, var(--paper) 0%, var(--paper) 45%, var(--paper-shade) 100%);
    box-shadow: inset 0 0 0 1px #d0d2d4;
  }

  .monogram {
    position: absolute; left: 0; right: 0;
    text-align: center; color: var(--accent);
    font-weight: 800; line-height: 1; font-size: 124px;
    letter-spacing: 2px;
  }
  .card--front .monogram { top: 86px; }
  .card--back .monogram { top: 79px; }

  .tagline {
    position: absolute; left: 0; right: 0; top: 198px;
    text-align: center; color: var(--accent);
    font-weight: 800; font-size: 15px; letter-spacing: 7px;
    padding-left: 7px;
  }
  .tagline .dark { color: var(--ink); }

  .strip {
    position: absolute; left: 0; right: 0; top: 242px; height: 20px;
    background: var(--strip);
    display: flex; align-items: center; justify-content: center;
    line-height: 1;
  }
  .strip__name {
    color: var(--accent); font-weight: 600; font-size: 12.5px;
    letter-spacing: 5.6px; padding-left: 5.6px;
  }
  .strip__name .light { color: var(--light); }
  .strip__contact { color: var(--accent); font-weight: 600; font-size: 11px; letter-spacing: 0.3px; }
  .strip__divider { color: var(--muted); margin: 0 10px; font-size: 10px; }
</style>
</head>
<body>
<main class="sheet">
  <section class="card card--front" aria-label="Card front">
    <div class="monogram">ML</div>
    <div class="strip">
      <p class="strip__name">MARCUS LINDQVIST <span class="light">PHOTO</span>GRAPHY</p>
    </div>
  </section>

  <section class="card card--back" aria-label="Card back">
    <div class="monogram">ML</div>
    <p class="tagline"><span class="dark">PHOTO</span>GRAPHY</p>
    <div class="strip">
      <span class="strip__contact">INFO@MARCUSLVQPHOTO.COM</span>
      <span class="strip__divider">|</span>
      <span class="strip__contact">555.214.3870</span>
      <span class="strip__divider">|</span>
      <span class="strip__contact">WWW.MARCUSLVQPHOTO.COM</span>
    </div>
  </section>
</main>
</body>
</html>
```